washable paper bags and accessories

We are three sisters who have discovered a mutual love of bags made from washable paper. It is a brand new business venture for bags, handbags, cosmetic bags, and home storage solutions and décor all made with washable paper.
We would like to have white crumpled paper as a background for both sides. Front of card with the words "wild plum folk" only in "bohemian typewriter regular" font. Back of card with appointment style format for our next pop up stall
Target Market(s)
mums, females
Industry/Entity Type
Business
Contact Information for Business Card
ph: 0491285364
email:wildplumfolk@postnestmail.net

```html
<!DOCTYPE html>
<html lang="en">
<head>
<meta charset="utf-8">
<title>Wild plum folk – business card</title>
<link rel="stylesheet" href="https://fonts.googleapis.com/css2?family=Special+Elite&display=swap">
<style>
  :root {
    --teal: #17b39b;
    --ink: #1a1a1a;
    --page: #ffffff;
    --paper-light: #f6f8f9;
    --paper-mid: #e3e8eb;
    --paper-shade: #d2dadf;
    --rule-green: #2e9a6c;
  }
  * { box-sizing: border-box; margin: 0; padding: 0; }
  html, body {
    width: 852px;
    height: 1200px;
    overflow: hidden;
    background: var(--page);
  }
  .sheet {
    position: relative;
    width: 852px;
    height: 1200px;
    font-family: "Special Elite", "Courier New", monospace;
    color: var(--ink);
  }
  .card {
    position: absolute;
    left: 9px;
    width: 842px;
    height: 522px;
    border: 3px solid var(--ink);
    overflow: hidden;
  }
  .card--front { top: 0; }
  .card--back { top: 677px; }

  .paper {
    position: absolute;
    inset: 0;
    background:
      linear-gradient(135deg, transparent 0 30%, rgba(210,218,223,0.45) 31%, transparent 40% 60%, rgba(210,218,223,0.35) 62%, transparent 70%),
      linear-gradient(45deg, transparent 0 45%, rgba(227,232,235,0.7) 48%, transparent 55%),
      radial-gradient(ellipse at 30% 40%, var(--paper-light), var(--paper-mid) 70%, var(--paper-shade));
  }
  .band {
    position: absolute;
    left: 0;
    right: 0;
    background: var(--teal);
  }
  .band--top {
    top: 0;
    height: 22px;
    border-bottom: 2px solid var(--ink);
  }
  .band--bottom {
    bottom: 0;
    border-top: 2px solid var(--ink);
  }
  .card--front .band--bottom { height: 100px; }
  .card--back .band--bottom { height: 87px; }

  .brand-name {
    position: absolute;
    top: 118px;
    left: 0;
    right: 0;
    text-align: center;
    font-size: 64px;
    line-height: 1.12;
    letter-spacing: 1px;
  }
  .contact {
    position: absolute;
    left: 232px;
    top: 16px;
    font-size: 19px;
    line-height: 1.75;
  }

  .appointment {
    position: absolute;
    top: 120px;
    left: 0;
    right: 0;
    text-align: center;
  }
  .appointment__lead {
    font-size: 38px;
    letter-spacing: 1px;
  }
  .appointment__title {
    margin-top: 30px;
    font-size: 36px;
    letter-spacing: 2px;
  }
  .write-line {
    position: absolute;
    left: 50px;
    top: 356px;
    width: 740px;
    height: 8px;
  }
</style>
</head>
<body>
<main class="sheet">
  <section class="card card--front">
    <div class="paper" role="img" aria-label="White crumpled paper texture"></div>
    <div class="band band--top"></div>
    <h1 class="brand-name">Wild plum<br>folk</h1>
    <div class="band band--bottom">
      <p class="contact">Phone: 0491285364<br>Email: wildplumfolk@postnestmail.net</p>
    </div>
  </section>

  <section class="card card--back">
    <div class="paper" role="img" aria-label="White crumpled paper texture"></div>
    <div class="band band--top"></div>
    <div class="appointment">
      <p class="appointment__lead">your next</p>
      <p class="appointment__title">APPOINTMENT</p>
    </div>
    <svg class="write-line" viewBox="0 0 740 8" aria-hidden="true">
      <line x1="0" y1="1.5" x2="740" y2="1.5" stroke="var(--ink)" stroke-width="2"/>
      <line x1="0" y1="6" x2="740" y2="6" stroke="var(--rule-green)" stroke-width="1.5"/>
    </svg>
    <div class="band band--bottom"></div>
  </section>
</main>
</body>
</html>
```